Varelio Soins: Symposium annuel 2018

You created the flyer "Atelier des pairs" for us at the beginning of the year. We would like to work in a new version. More details can be found in the briefing! Flyer (red, gray, black) - flyer wants to be white! - Flyer wants to be White! All further information can be found in the document in the appendix!

```html
<!DOCTYPE html>
<html lang="fr">
<head>
<meta charset="utf-8">
<title>Varelio Soins – Symposium annuel 2018</title>
<link href="https://fonts.googleapis.com/css2?family=Montserrat:wght@500;600;700&family=Open+Sans:ital,wght@0,400;0,600;1,400;1,600&display=swap" rel="stylesheet">
<style>
  :root{
    --red:#e30613;
    --red-dark:#b8000c;
    --ink:#111;
    --grey:#5a5a5a;
    --stage:#d2d2d2;
    --paper:#fff;
  }
  *{margin:0;padding:0;box-sizing:border-box}
  html,body{width:1200px;height:1200px;overflow:hidden;background:var(--stage)}
  .flyer{position:absolute;left:0;top:176px;width:1200px;height:849px;background:var(--paper);
    font-family:"Open Sans",sans-serif;color:var(--ink);overflow:hidden}
  .flyer > *{position:absolute}
  .backdrop{left:360px;top:60px;width:420px;height:760px;
    background:radial-gradient(ellipse at center,rgba(200,200,200,.28),rgba(255,255,255,0) 70%)}
  .title{left:40px;top:24px;font-family:"Montserrat",sans-serif;font-weight:700;color:var(--red);line-height:1}
  .title .l1{display:block;font-size:50px;letter-spacing:-1px}
  .title .l2{display:block;font-size:64px;margin-top:8px;letter-spacing:-1px}
  .date-box{left:39px;top:155px;width:496px;height:105px;border:3px solid var(--red);border-radius:26px;
    text-align:center;font-family:"Montserrat",sans-serif;font-weight:700;line-height:1.12}
  .date-box .day{color:var(--red);font-size:40px;margin-top:5px;display:block}
  .date-box .hours{font-size:40px;display:block}
  .venue{left:50px;top:268px;font-family:"Montserrat",sans-serif;font-weight:600;font-size:35px}
  .credits{left:32px;top:331px;width:204px;height:46px;background:linear-gradient(var(--red),var(--red-dark));
    color:#fff;font-family:"Montserrat",sans-serif;font-weight:600;font-size:29px;padding-left:20px;line-height:46px;
    border-radius:8px 0 0 8px}
  .societies{left:32px;top:391px;font-style:italic;font-weight:600;font-size:26px;line-height:39px}
  .inscription{left:32px;top:483px;color:var(--red);font-family:"Montserrat",sans-serif;font-weight:600;font-size:36px}
  .field{font-family:"Montserrat",sans-serif;font-weight:600;font-size:20px;white-space:nowrap}
  .field.name{left:32px;top:535px}
  .field.stamp{left:36px;top:580px}
  .return{left:27px;top:623px;font-style:italic;font-weight:600;font-size:28px}
  .contact{left:27px;font-style:italic;font-size:25px;display:flex;align-items:center;gap:8px}
  .contact.fax{top:665px}
  .contact.mail{top:698px}
  .contact .hl{color:var(--red)}
  .brand{left:27px;top:766px;display:flex;align-items:center;gap:8px;
    font-family:"Montserrat",sans-serif;font-weight:700;font-size:26px;color:var(--ink);letter-spacing:1px}
  .brand .mark{width:22px;height:22px;background:var(--red)}
  .programme-title{left:663px;top:31px;font-family:"Montserrat",sans-serif;font-weight:600;font-size:17.5px;letter-spacing:-.3px}
  .time{left:664px;width:124px;height:32px;background:linear-gradient(var(--red),var(--red-dark));color:#fff;
    font-family:"Montserrat",sans-serif;font-weight:600;font-size:16px;text-align:center;line-height:32px;
    border-radius:4px 4px 12px 4px}
  .talk-title{left:804px;font-family:"Montserrat",sans-serif;font-weight:600;font-size:19px;color:var(--red);line-height:22px}
  .talk-speaker{left:804px;font-size:17.5px;line-height:22px;color:#222}
  .sponsors{left:664px;top:790px;width:487px;display:flex;align-items:center;justify-content:space-between;
    font-family:"Montserrat",sans-serif;font-weight:600;font-size:17px;color:var(--grey)}
</style>
</head>
<body>
<main class="flyer">
  <div class="backdrop" role="img" aria-label="Illustration pâle du système lymphatique humain en arrière-plan"></div>

  <h1 class="title"><span class="l1">SYMPOSIUM ANNUEL</span><span class="l2">VARELIO SOINS</span></h1>

  <div class="date-box"><span class="day">27 septembre 2018</span><span class="hours">de 14h00 à 18h00</span></div>
  <div class="venue">Auditoire Henri Morel, HRL</div>
  <div class="credits">Crédits : 4</div>
  <div class="societies">Société Romande de Phlébologie<br>Médicine interne Générale</div>

  <h2 class="inscription">Inscription</h2>
  <div class="field name">Nom :......................................... Prénom:...........................................</div>
  <div class="field stamp">Timbre et signature : .....................................................................</div>

  <div class="return">Bulletin d’inscription à retourner :</div>
  <div class="contact fax">
    <svg width="24" height="22" viewBox="0 0 24 22" aria-hidden="true"><rect x="6" y="1" width="12" height="6" fill="none" stroke="#e30613" stroke-width="2"/><rect x="1" y="7" width="22" height="9" rx="2" fill="#e30613"/><rect x="6" y="13" width="12" height="8" fill="#fff" stroke="#e30613" stroke-width="2"/></svg>
    <span>par fax <span class="hl">021 555 18 42</span> ou</span>
  </div>
  <div class="contact mail">
    <svg width="24" height="18" viewBox="0 0 24 18" aria-hidden="true"><rect x="1" y="1" width="22" height="16" fill="#e30613"/><path d="M1 1l11 9 11-9M1 17l8-8M23 17l-8-8" stroke="#fff" stroke-width="1.6" fill="none"/></svg>
    <span>e-mail : <span class="hl">info@varelio-soins.ch</span></span>
  </div>

  <div class="brand"><span class="mark"></span>VARELIO SOINS</div>

  <h2 class="programme-title">ACTUALISATION DES CONNAISSANCES EN LYMPHOLOGIE</h2>

  <div class="time" style="top:62px">14:00-14:10</div>
  <h3 class="talk-title" style="top:73px">Bienvenue</h3>

  <div class="time" style="top:103px">14:00-14:10</div>
  <h3 class="talk-title" style="top:105px">A la découverte des lymphatiques :<br>place de l’IRM</h3>
  <p class="talk-speaker" style="top:153px">Pr A. Ferrandi, University of Lucca, Italy</p>

  <div class="time" style="top:176px">14:45-15:15</div>
  <h3 class="talk-title" style="top:177px">Une entité nouvelle : le système</h3>
  <p class="talk-speaker" style="top:201px">M. J. Valmont, Service d’Angiologie,<br>HRL, Lausanne</p>

  <div class="time" style="top:246px">15:20 - 15:50</div>
  <h3 class="talk-title" style="top:248px">Approche psychosomatique<br>du lymphœdème</h3>
  <p class="talk-speaker" style="top:291px">Dr K. Brauner, biologiste et psychologue<br>cabinet spécialisé en psycho-<br>oncologie, Freiburg, Allemagne</p>

  <div class="time" style="top:356px">15:50 - 16:10</div>
  <h3 class="talk-title" style="top:366px">Pause</h3>

  <div class="time" style="top:400px">15:20 - 15:50</div>
  <h3 class="talk-title" style="top:398px">Prévenir le lymphœdème lors de<br>la chirurgie oncologique:<br>l’expérience LYMPHA</h3>
  <p class="talk-speaker" style="top:472px">Pr R. Castelli, Université de<br>Parma, Italie</p>

  <div class="time" style="top:514px">16:45 - 17:15</div>
  <h3 class="talk-title" style="top:521px">Quand traiter le lymphœdème par<br>voie chirurgicale ?</h3>
  <p class="talk-speaker" style="top:573px">Dr L. Ravenna, Service de chirurgie<br>plastique et reconstructive, HRL,<br>Lausanne</p>

  <div class="time" style="top:641px">16:45 - 17:15</div>
  <h3 class="talk-title" style="top:643px">Le vaisseau lymphatique artificiel :<br>mythe ou réalité ?</h3>
  <p class="talk-speaker" style="top:692px">Pr C. Morand, Service d’Angiologie,<br>HRL, Lausanne</p>

  <div class="time" style="top:736px">17 :55 - 18.00</div>
  <h3 class="talk-title" style="top:744px">Conclusion</h3>

  <div class="sponsors">
    <span>Calyndo</span><span>Noverrin</span><span>Plessa Care</span><span>Trivelta</span><span>Quessol</span>
  </div>
</main>
</body>
</html>
```